velmorino.eu :: Design ideas (no coding) for key pages of Personalized greeting cards online store

We need your vision on modern, clean, easy to read user interface (UI) for online service of personalized printed products, like greeting cards, postcards, fridge magnets, clips and etc.
Your vision should include UI presentation for:
- Home page with login (including soc nets)
- Product Designer page
- Cart pages (products and address selection)
- Example of general internal page (pricing, terms, etc)
- Artist info and portfolio page
We are looking for ideas we will love, NOT complete design of a whole site.
Top design/vision will we used as a basement for separate contract on complete design of the site.

UI should be based on existing functionality with some extent. It should not break ideas or methods used on prototype but designers are free to offer own product presentations, designer’s layout and cart views.

Prototype:
English: http://velmorino.eu
Russian: http://velmorino.ru
Lithuanian: http://velmorino.lt

Target Market(s)

People of 16-45 y.o. who likes to be distinctive, personal.

Industry/Entity Type

Store

Requirements
Must have
• Your work should meet attached requirements.
Site is multilingual. Wording should assume varieties in length on different languages.
Clean and easy to read UI
Flat design preferrably
Should be based on assets which are free or available for royalty-free licensing
Should not have
• heavy, meaningless 3D and shadow effects
Show NOT copy sites like: plonkra.com, tarnwick.co.uk

```html
<!DOCTYPE html>
<html lang="en">
<head>
<meta charset="utf-8">
<title>velmorino – Greeting Cards Store</title>
<link rel="stylesheet" href="https://fonts.googleapis.com/css2?family=Montserrat:wght@400;600;700&family=Open+Sans:wght@400;600&display=swap">
<style>
:root{
  --yellow:#f6d838;
  --ink:#2b2b2b;
  --text:#555;
  --muted:#8a8a8a;
  --line:#e2e2e2;
  --panel:#efefef;
  --footer:#f4f3f3;
  --red:#e3382c;
  --dark:#333;
  --sky1:#2e9fd8;
  --sky2:#7cc9ee;
}
*{box-sizing:border-box;margin:0;padding:0}
html,body{width:1200px;height:2289px;overflow:hidden;background:#fff}
body{font-family:"Open Sans",Arial,sans-serif;color:var(--text);position:relative}
.wrap{position:absolute;left:140px;width:920px}
.topbar{position:absolute;top:0;left:0;width:1200px;height:29px;background:var(--yellow);font-size:12px;color:var(--ink)}
.topbar .lang{position:absolute;left:140px;top:6px;display:flex;gap:22px}
.topbar .account{position:absolute;right:140px;top:6px;display:flex;gap:18px;align-items:center}
.topbar svg{vertical-align:-2px;margin-right:5px}
.header{position:absolute;top:29px;left:0;width:1200px;height:92px;background:#fff}
.logo{position:absolute;left:145px;top:14px;display:flex;flex-direction:column;align-items:center;gap:4px}
.logo .mark{width:46px;height:40px;background:#c8443a}
.logo .name{font-family:"Montserrat",sans-serif;font-weight:600;font-size:14px;color:var(--ink)}
.nav{position:absolute;right:140px;top:14px;display:flex;gap:24px;font-family:"Montserrat",sans-serif;font-size:13px;color:var(--ink);text-transform:uppercase}
.search{position:absolute;right:140px;top:48px;width:186px;height:38px;border:1px solid var(--line);font-size:10px;color:var(--muted);padding:12px 8px}
.search svg{position:absolute;right:8px;top:12px}
.hero{position:absolute;top:124px;left:0;width:1200px;height:359px;background:linear-gradient(180deg,var(--sky1),var(--sky2) 55%,#1d5b7a 80%,#123c52)}
.hero .deco{position:absolute;inset:0}
.hero .line{position:absolute;left:140px;background:rgba(220,240,250,.88);font-family:"Montserrat",sans-serif;font-size:28px;color:#1e3d58;padding:8px 20px}
.hero .line.one{top:70px;width:610px}
.hero .line.two{top:124px;width:232px;background:rgba(40,120,170,.75);color:#fff}
.dots{position:absolute;left:560px;bottom:8px;display:flex;gap:4px}
.dots i{width:6px;height:6px;background:#fff;opacity:.7;display:block}
.title{position:absolute;left:140px;width:920px;height:42px;border:1px solid var(--line);border-left:4px solid var(--ink);box-shadow:0 2px 3px rgba(0,0,0,.06);font-family:"Montserrat",sans-serif;font-weight:700;font-size:17px;color:var(--ink);padding:10px 8px;text-transform:uppercase}
.title .arrows{position:absolute;right:8px;top:10px;display:flex;gap:10px}
.title .arrows span{width:16px;height:16px;display:flex;align-items:center;justify-content:center;background:#fff}
.title .arrows span.on{background:var(--ink)}
.filters{position:absolute;top:563px;left:140px;width:920px;display:flex;gap:20px}
.filter{width:168px}
.filter h3{font-family:"Montserrat",sans-serif;font-size:16px;color:var(--ink);font-weight:600;text-transform:uppercase;border-bottom:2px solid var(--line);padding-bottom:14px;margin-bottom:14px}
.filter .box{background:var(--panel);height:95px;padding:12px 10px;font-size:12px;color:var(--text);position:relative}
.filter li{list-style:none;display:flex;align-items:center;gap:12px;height:26px}
.chk{width:10px;height:10px;border:1px solid #9a9a9a;background:#fff;display:inline-block;position:relative}
.scroll{position:absolute;right:12px;top:30px;width:3px;height:30px;background:#666}
.swatches{display:grid;grid-template-columns:repeat(6,14px);gap:12px 7px}
.swatches i{width:14px;height:14px;display:block}
.range{position:relative;height:100%}
.range .bar{position:absolute;left:6px;right:6px;top:26px;height:4px;background:var(--yellow)}
.range .bar:before,.range .bar:after{content:"";position:absolute;top:-5px;width:4px;height:14px;background:#444}
.range .bar:before{left:0}.range .bar:after{right:0}
.range p{position:absolute;top:44px;width:100%;text-align:center;font-size:10px}
.grid{position:absolute;left:140px;width:920px;display:flex;gap:23px}
.card{width:212px}
.card .pic{height:277px}
.card .strip{height:6px;display:flex}
.card .strip i{flex:1}
.card .meta{border-left:1px solid var(--line);border-right:1px solid var(--line);font-size:11px;color:var(--text);padding:4px 8px;height:58px;display:grid;grid-template-columns:1fr auto;row-gap:10px;align-content:start;padding-top:8px}
.card .meta span:nth-child(even){text-align:right}
.card .act{display:flex;height:38px;border:1px solid var(--line)}
.card .act div{flex:1;display:flex;align-items:center;justify-content:center;font-size:11px;color:var(--ink);gap:6px}
.card .act .price{color:var(--red);border-left:1px solid var(--line)}
.formats{position:absolute;top:1637px;left:140px;width:920px;display:flex;justify-content:space-between}
.format{width:252px}
.format h3{font-family:"Montserrat",sans-serif;font-weight:700;font-size:18px;color:var(--ink);text-transform:uppercase;border-bottom:2px solid var(--line);padding-bottom:8px;margin-bottom:10px}
.format .pic{height:115px}
.format p{font-size:14px;line-height:27px;color:var(--text);margin-top:12px;height:135px;overflow:hidden}
.footer{position:absolute;top:1994px;left:0;width:1200px;height:258px;background:var(--footer)}
.col{position:absolute;top:22px}
.col h4{font-family:"Montserrat",sans-serif;font-size:16px;font-weight:600;color:var(--ink);margin-bottom:10px}
.about{left:140px;width:220px;font-size:12px;line-height:19px}
.news{left:389px;width:200px;font-size:12px;line-height:18px}
.news .field{width:184px;height:38px;border:1px solid var(--line);background:#fff;margin-top:16px;font-size:10px;color:var(--muted);padding:12px 8px}
.news .btn{width:102px;height:34px;background:#555;color:#fff;font-size:12px;display:flex;align-items:center;justify-content:center;margin-top:14px}
.social{display:flex;gap:9px;margin-top:12px}
.social i{width:42px;height:42px;border-radius:50%;background:#3a3a3a;display:block}
.links{left:647px;font-size:12px;line-height:28px}
.links h4{margin-bottom:0}
.contact{left:880px;width:185px;font-size:12px;line-height:19px}
.contact .row{display:flex;gap:12px;margin-bottom:14px}
.contact b{font-weight:600;color:var(--ink)}
.copy{position:absolute;top:2252px;left:0;width:1200px;height:37px;text-align:center;font-size:12px;color:var(--ink);padding-top:12px}
</style>
</head>
<body>

<div class="topbar">
  <div class="lang"><span>English ⌄</span><span>EURO ⌄</span></div>
  <div class="account">
    <span><svg width="12" height="12" viewBox="0 0 12 12"><circle cx="6" cy="3.5" r="2.5" fill="#2b2b2b"/><path d="M1 12c0-3 2-5 5-5s5 2 5 5z" fill="#2b2b2b"/></svg>Register</span><span>/</span>
    <span><svg width="10" height="12" viewBox="0 0 10 12"><rect x="0" y="5" width="10" height="7" fill="#2b2b2b"/><path d="M2 5V3a3 3 0 0 1 6 0v2" stroke="#2b2b2b" stroke-width="1.5" fill="none"/></svg>Login</span>
    <span><svg width="13" height="12" viewBox="0 0 13 12"><path d="M0 1h2l2 7h7l2-5H3" stroke="#2b2b2b" stroke-width="1.4" fill="none"/><circle cx="5" cy="10.5" r="1.3" fill="#2b2b2b"/><circle cx="10" cy="10.5" r="1.3" fill="#2b2b2b"/></svg>Cart (0)</span>
    <span><svg width="12" height="12" viewBox="0 0 12 12"><rect x=".5" y=".5" width="11" height="11" fill="none" stroke="#2b2b2b"/><path d="M3 6l2 2 4-4" stroke="#2b2b2b" stroke-width="1.4" fill="none"/></svg>Wishlist</span>
  </div>
</div>

<header class="header">
  <div class="logo"><span class="mark"></span><span class="name">velmorino</span></div>
  <nav class="nav"><span>All Medias</span><span>Greeting Cards</span><span>Square Cards</span><span>Postcards</span><span>Contact Us</span></nav>
  <div class="search">Product By Keyword Search
    <svg width="12" height="12" viewBox="0 0 12 12"><circle cx="5" cy="5" r="3.8" stroke="#555" stroke-width="1.4" fill="none"/><path d="M8 8l3.5 3.5" stroke="#555" stroke-width="1.5"/></svg>
  </div>
</header>

<section class="hero">
  <div class="deco" role="img" aria-label="Winter illustration with snowy forest, wrapped gift boxes and hanging red, pink and green SALE tags"></div>
  <div class="line one">The Individual Greeting Cards According</div>
  <div class="line two">To Your Mood</div>
  <div class="dots"><i></i><i></i><i></i><i></i></div>
</section>

<div class="title" style="top:506px">Search Products</div>

<div class="filters">
  <div class="filter"><h3>Themes</h3>
    <ul class="box">
      <li><span class="chk"></span>All</li>
      <li><span class="chk"><svg width="10" height="10" viewBox="0 0 10 10" style="position:absolute;left:0;top:-1px"><path d="M1 5l3 3 5-7" stroke="#333" stroke-width="1.6" fill="none"/></svg></span>Bears</li>
      <li><span class="chk"></span>Birthday</li>
      <span class="scroll"></span>
    </ul>
  </div>
  <div class="filter"><h3>By Two Colors</h3>
    <div class="box"><div class="swatches">
      <i style="background:#e7d6a3"></i><i style="background:#c9c9c9"></i><i style="background:#8f8f8f"></i><i style="background:#f2a8b8"></i><i style="background:#9cc3e8"></i><i style="background:#b7a4d6"></i>
      <i style="background:#8a5a2b"></i><i style="background:#7db83a"></i><i style="background:#2f6fc0"></i><i style="background:#3a3a3a"></i><i style="background:#d93a2c"></i><i style="background:#2d8a4b"></i>
      <i style="background:#45c3cf"></i><i style="background:#f07a1e"></i><i style="background:#f5c51c"></i><i style="background:#fff"></i><i style="background:#e54b8b"></i><i style="background:#3c4a9a"></i>
    </div></div>
  </div>
  <div class="filter"><h3>Price From - To</h3>
    <div class="box"><div class="range"><span class="bar"></span><p>Price: $0 — $100</p></div></div>
  </div>
  <div class="filter"><h3>Shape</h3>
    <ul class="box"><li><span class="chk"></span>Square</li><li><span class="chk"></span>Normal</li><li><span class="chk"></span>Mini Cards</li></ul>
  </div>
  <div class="filter"><h3>Type</h3>
    <ul class="box"><li><span class="chk"></span>Greeting cards</li><li><span class="chk"></span>Postcards</li><li><span class="chk"></span>Fridge Magnets</li></ul>
  </div>
</div>

<div class="title" style="top:735px">Featured Products
  <div class="arrows"><span><svg width="8" height="10" viewBox="0 0 8 10"><path d="M6 1L2 5l4 4" stroke="#333" stroke-width="1.6" fill="none"/></svg></span><span class="on"><svg width="8" height="10" viewBox="0 0 8 10"><path d="M2 1l4 4-4 4" stroke="#fff" stroke-width="1.6" fill="none"/></svg></span></div>
</div>

<div class="grid" style="top:797px">
  <article class="card">
    <div class="pic" role="img" aria-label="Black and white photo of two monkeys" style="background:linear-gradient(160deg,#d8d8d8,#6a6a6a)"></div>
    <div class="strip"><i style="background:#ddd"></i><i style="background:#aaa"></i><i style="background:#666"></i><i style="background:#222"></i><i style="background:#6b3d8c"></i></div>
    <div class="meta"><span>Fern Hall Studio</span><span>Bezdziones</span><span>Juodai baltos</span><span>Nuotraukos</span></div>
    <div class="act"><div>🛒 Add to cart</div><div class="price">€ 0.99</div></div>
  </article>
  <article class="card">
    <div class="pic" role="img" aria-label="Black and white photo of two penguins" style="background:linear-gradient(160deg,#f2f2f2,#8c8c8c)"></div>
    <div class="strip"><i style="background:#eee"></i><i style="background:#999"></i><i style="background:#333"></i><i style="background:#111"></i><i style="background:#4bbccc"></i></div>
    <div class="meta"><span>Fern Hall Studio</span><span>Pingvinai</span><span>Nuotraukos</span><span>Meile</span></div>
    <div class="act"><div>🛒 Add to cart</div><div class="price">€ 0.99</div></div>
  </article>
  <article class="card">
    <div class="pic" role="img" aria-label="Photo of a puppy with a lollipop and party crown" style="background:linear-gradient(170deg,#d99cb0,#b05a3a 70%,#6a3a8a)"></div>
    <div class="strip"><i style="background:#c0533a"></i><i style="background:#e27fa0"></i><i style="background:#7a2e6b"></i><i style="background:#222"></i><i style="background:#8ccde0"></i></div>
    <div class="meta"><span>Fern Hall Studio</span><span>Bezdziones</span><span>Juodai baltos</span><span>Nuotraukos</span></div>
    <div class="act"><div>🛒 Add to cart</div><div class="price">€ 0.99</div></div>
  </article>
  <article class="card">
    <div class="pic" role="img" aria-label="Photo of sea shells and a red starfish" style="background:linear-gradient(160deg,#d9b08a,#a05a3a 60%,#c73a2c)"></div>
    <div class="strip"><i style="background:#c73a2c"></i><i style="background:#e0b08a"></i><i style="background:#5a3a2a"></i><i style="background:#222"></i><i style="background:#8ccde0"></i></div>
    <div class="meta"><span>Fern Hall Studio</span><span>Sveikinimai</span><span>Šunys&nbsp;&nbsp;Gimtadienis</span><span>Nuotraukos</span></div>
    <div class="act"><div>🛒 Add to cart</div><div class="price">€ 0.99</div></div>
  </article>
</div>

<div class="title" style="top:1189px">The Best Flowers From Top Collections
  <div class="arrows"><span><svg width="8" height="10" viewBox="0 0 8 10"><path d="M6 1L2 5l4 4" stroke="#333" stroke-width="1.6" fill="none"/></svg></span><span class="on"><svg width="8" height="10" viewBox="0 0 8 10"><path d="M2 1l4 4-4 4" stroke="#fff" stroke-width="1.6" fill="none"/></svg></span></div>
</div>

<div class="grid" style="top:1254px">
  <article class="card">
    <div class="pic" role="img" aria-label="Illustration of white flowers on a red patterned background" style="background:radial-gradient(circle at 50% 45%,#f2e6c0 0,#e0b04a 28%,#d2402c 55%)"></div>
    <div class="strip"><i style="background:#d2402c"></i><i style="background:#f2e6c0"></i><i style="background:#7db83a"></i><i style="background:#e0b04a"></i><i style="background:#222"></i></div>
    <div class="meta"><span>Fern Hall Studio</span><span>Gele</span></div>
    <div class="act"><div>🛒 Add to cart</div><div class="price">€ 0.99</div></div>
  </article>
  <article class="card">
    <div class="pic" role="img" aria-label="Watercolour illustration of a flower basket" style="background:radial-gradient(circle at 50% 45%,#f2a07a 0,#d6b8d8 40%,#d8ecf2 70%)"></div>
    <div class="strip"><i style="background:#6b9bd1"></i><i style="background:#f07a4a"></i><i style="background:#e7b44a"></i><i style="background:#7db83a"></i><i style="background:#a45ab0"></i></div>
    <div class="meta"><span>Fern Hall Studio</span><span>Puokste</span><span>Krepšeliai</span><span>Geles</span></div>
    <div class="act"><div>🛒 Add to cart</div><div class="price">€ 0.99</div></div>
  </article>
  <article class="card">
    <div class="pic" role="img" aria-label="Watercolour illustration of colourful flowers" style="background:radial-gradient(circle at 50% 50%,#e8a0d8 0,#f2e06a 30%,#f4f6f0 65%)"></div>
    <div class="strip"><i style="background:#d05ab0"></i><i style="background:#f2d03a"></i><i style="background:#4a8ad8"></i><i style="background:#7db83a"></i><i style="background:#e8a0d8"></i></div>
    <div class="meta"><span>Fern Hall Studio</span><span>Sveikinimai</span><span>Geles</span><span>Sveikinimai</span></div>
    <div class="act"><div>🛒 Add to cart</div><div class="price">€ 0.99</div></div>
  </article>
  <article class="card">
    <div class="pic" role="img" aria-label="Illustration of a sunflower on a pale blue background" style="background:radial-gradient(circle at 50% 30%,#f2c21c 0,#e0a020 22%,#cfeaf0 45%,#e8f4f0 80%)"></div>
    <div class="strip"><i style="background:#f2c21c"></i><i style="background:#5a3a1a"></i><i style="background:#3a8a3a"></i><i style="background:#cfeaf0"></i><i style="background:#222"></i></div>
    <div class="meta"><span>Fern Hall Studio</span><span>Saulegrazos</span><span>Geles</span><span></span></div>
    <div class="act"><div>🛒 Add to cart</div><div class="price">€ 0.99</div></div>
  </article>
</div>

<section class="formats">
  <div class="format"><h3>Square</h3>
    <div class="pic" role="img" aria-label="Photo of square greeting cards on a table" style="background:linear-gradient(120deg,#e8d2b0,#b89a78 60%,#5a5a6a)"></div>
    <p>"But I must explain to you how all this mistaken idea of denouncing pleasure and praising pain was born and I will give you a complete account of the system, and expound the actual teachings of the great explorer of the</p>
  </div>
  <div class="format"><h3>Normal</h3>
    <div class="pic" role="img" aria-label="Photo of standing greeting cards" style="background:linear-gradient(120deg,#c8b498,#e8dccb 50%,#8a9a7a)"></div>
    <p>"But I must explain to you how all this mistaken idea of denouncing pleasure and praising pain was born and I will give you a complete account of the system, and expound the actual teachings of the great explorer of the</p>
  </div>
  <div class="format"><h3>Mini Cards</h3>
    <div class="pic" role="img" aria-label="Photo of small cards spread on a table" style="background:linear-gradient(120deg,#e0c8a8,#a88a6a 55%,#6a6a78)"></div>
    <p>"But I must explain to you how all this mistaken idea of denouncing pleasure and praising pain was born and I will give you a complete account of the system, and expound the actual teachings of the great explorer of the</p>
  </div>
</section>

<footer class="footer">
  <div class="col about"><h4>About us</h4>
    <p>At vero eos et accusamus et iusto odio dignissimos ducimus qui blanditiis praesentium voluptatum deleniti atque corrupti quos dolores et quas molestias excepturi sint occaecati cupiditate non provident, similique sunt in culpa qui officia dese.</p>
  </div>
  <div class="col news"><h4>Newsletter</h4>
    <p>Sign up for our e-mail newsletter!</p>
    <div class="field">Your E-mail</div>
    <div class="btn">Submit</div>
    <div class="social"><i></i><i></i><i></i><i></i></div>
  </div>
  <div class="col links"><h4>More Information</h4>
    <div>Home</div><div>About us</div><div>How It Works</div><div>Prices</div><div>Rules</div><div>Contact Us</div>
  </div>
  <div class="col contact"><h4>Contact Info</h4>
    <div class="row"><svg width="12" height="12" viewBox="0 0 12 12"><path d="M6 1L1 6h2v5h6V6h2z" fill="#aaa"/></svg><div><b>Address :</b><br>262 Lorem Ipsum ,<br>dummy text Contrary to</div></div>
    <div class="row"><svg width="12" height="10" viewBox="0 0 12 10"><rect width="12" height="10" fill="#aaa"/><path d="M0 0l6 5 6-5" stroke="#fff" fill="none"/></svg><div><b>Email:</b><br>info@velmorino.eu</div></div>
    <div class="row"><svg width="12" height="12" viewBox="0 0 12 12"><path d="M2 1l2 0 1 3-1.5 1a7 7 0 0 0 3.5 3.5L8 7l3 1v2a1 1 0 0 1-1 1C5 11 1 7 1 2a1 1 0 0 1 1-1z" fill="#aaa"/></svg><div><b>Phone :</b><br>(00)11-222-5566</div></div>
  </div>
</footer>
<div class="copy">© COPYRIGHT 2014 - VELMORINO.EU</div>

</body>
</html>
```